Website Design for Solar Panel Company

We are working with a company called BrightVX.

Some sites to use for content/competitors and inspiration:
https://www.dawnmill.com
https://prod.cdn-prod.raylokt.com
https://mossbeamvolt.net
https://www.quorvin.com/solarpanels

Thank you for taking the time to consider designing a website for us. We are web developers based in Stockton, CA, USA. Most of our projects go through the same process. Understanding this process may help you win a project with us. We custom-code all of our websites in-house. We don’t have any requirements as to what tools you use for your design, but we prefer Figma files. For any design that we label as four-stars, we send it to the client for review. The client picks the final design they want us to use. Once we complete this process, we will continue to show additional clients all the four-star sites and purchase them later. Your designs will have multiple chances to sell. For better chances of success, we ask that you follow these guidelines.

IMAGES:
If you use any images or icons in the design, we ask that you have a link to the asset so we can purchase the image/icon. Most of the designs we submit do not have the customer’s images on them unless they have some great images. Be creative; show us the feeling you are trying to portray with your image choices. Use any royalty-free site you choose. We subscribe to Corvane and mainly use their images, but we can purchase images outside of Corvane. PLEASE NOTE: we will not submit designs to clients with watermarks on the images.

FONTS:
We ask that you identify the fonts used in the design. This can be done in a message if you want. We typically use Tivelo Fonts and Corvane Fonts.

CONTENT:
We're always open to different content and ideas. We often submit designs with stock images so the client can see our vision. We typically take pictures after the website launch to use their images with our vision. Lorem Ipsum is fine for paragraphs, but we ask that you write the headers in correct English. We want to be able to show the vision and identify the sections of the website.

INSPIRATION:
We typically add a couple of links in the brief of websites we like to help you get started in your design.

REVISIONS:
We do not often ask for revisions of the designs unless we see something in the design that may not appeal to the client. If there are slight changes that we want to make, we do that in the development process.

FEEDBACK:
We rarely give feedback on designs during the design process. We are working on many website projects and do not have the time to provide feedback. We usually respond if your request is well thought out and asks specific questions, but a note asking “feedback, please” usually goes unanswered.

```html
<!DOCTYPE html>
<html lang="en">
<head>
<meta charset="utf-8">
<title>BrightVX Energy Group</title>
<link rel="stylesheet" href="https://fonts.googleapis.com/css2?family=Poppins:wght@300;400;500;600;700;800;900&display=swap">
<style>
:root{
  --green:#3fae1e;
  --green-bright:#5fd62a;
  --green-dark:#1c6a10;
  --black:#000;
  --ink:#111;
  --card:#181818;
  --field:#1d1d1d;
  --line:#333;
  --white:#fff;
  --muted:#cfcfcf;
}
*{box-sizing:border-box;margin:0;padding:0}
html,body{width:1200px;height:5063px;overflow:hidden;background:var(--black);color:var(--white);font-family:'Poppins',sans-serif}
section,header,footer,nav{position:relative;width:1200px;overflow:hidden}
.abs{position:absolute}
.btn{display:inline-flex;align-items:center;justify-content:center;border-radius:40px;font-weight:500;text-transform:uppercase;color:var(--white)}
.btn-solid{background:linear-gradient(90deg,#2f9a17,var(--green-bright))}
.btn-outline{border:2px solid var(--white)}
.photo{position:absolute}

/* top bar */
.topbar{height:53px;background:var(--green)}
.topbar .call{left:745px;top:13px;display:flex;align-items:center;gap:10px;font-size:12px}
.topbar .call i{width:28px;height:28px;border:1.5px solid var(--white);border-radius:50%;display:flex;align-items:center;justify-content:center}
.topbar .cta{right:76px;top:0;width:182px;height:53px;background:#111;font-size:13px;display:flex;align-items:center;justify-content:center}

/* nav */
.nav{height:118px;background:var(--black)}
.logo{display:flex;align-items:center;gap:10px;font-weight:800;font-size:36px;letter-spacing:1px;color:var(--white);white-space:nowrap}
.logo i{width:24px;height:24px;border-radius:50%;background:var(--green-bright)}
.nav .logo{left:73px;top:35px}
.nav ul{list-style:none;display:flex;gap:46px;left:549px;top:50px;font-size:12.5px;font-weight:500}
.nav li.active{color:var(--green-bright)}

/* hero */
.hero{height:758px}
.hero .photo{inset:0;background:linear-gradient(180deg,#9fc6e6 0%,#d9e8f3 35%,#6d8fc0 55%,#23418a 78%,#142c6b 100%)}
.hero .copy{left:395px;width:760px;top:137px;text-align:center;color:#111}
.hero h2{font-weight:400;font-size:51px;line-height:1.1}
.hero h1{font-weight:800;font-size:50px;line-height:1.35;margin-top:6px;white-space:nowrap}
.hero p{font-size:17.5px;line-height:1.25;margin:22px auto 0;width:600px}
.hero .btn{margin-top:32px;width:188px;height:50px;font-size:12px}

/* features */
.features{height:259px;background:var(--black)}
.feature{top:50px;text-align:center;font-size:20.5px;line-height:1.35;font-weight:500}
.feature svg{display:block;margin:0 auto 10px}
.vdiv{top:53px;width:1px;height:112px;background:#555}

/* about */
.about{height:599px;background:linear-gradient(90deg,#2f9b17 0%,#3eae1e 28%,#237812 52%,#0a1f06 72%,#000 86%)}
.about h2{left:76px;top:118px;font-size:55px;font-weight:800}
.about .sub{left:80px;top:192px;font-size:20px;display:flex;align-items:center;gap:28px}
.about .sub b{width:104px;height:2px;background:var(--white)}
.about p{left:80px;top:268px;width:450px;font-size:13.5px;line-height:2}
.about .btn{left:78px;top:451px;width:194px;height:63px;font-size:15px}
.about .ring{left:563px;top:-15px;width:600px;height:600px;border-radius:50%;background:linear-gradient(200deg,#4a4a4a 0%,#1a1a1a 40%,#49b81f 80%)}
.about .photo{left:607px;top:42px;width:512px;height:512px;border-radius:50%;background:linear-gradient(180deg,#b8c6d6 0%,#8798ae 45%,#38404c 70%,#1a1f27 100%)}

/* section titles */
.title{text-align:center;width:1200px;left:0}
.title h2{font-size:56px;font-weight:800;line-height:1.1}
.title .sub{display:flex;justify-content:center;align-items:center;gap:20px;color:var(--green-bright);font-size:21px;margin-top:6px}
.title .sub b{width:108px;height:2px;background:var(--green-bright)}

/* services */
.services{height:819px;background:var(--black)}
.services .title{top:140px}
.svc{top:314px;width:333px;height:366px;background:var(--card);border:2px solid #2a2a2a;border-radius:20px}
.svc.featured{border-color:var(--green-bright)}
.svc .photo{left:8px;top:8px;width:313px;height:178px;border-radius:12px 12px 0 0;background:linear-gradient(160deg,#cfdde9 0%,#7b95b8 45%,#2b4676 100%)}
.svc .power{left:140px;top:156px;width:52px;height:52px;border-radius:50%;background:#0e0e0e;display:flex;align-items:center;justify-content:center}
.svc h3{top:232px;width:100%;text-align:center;color:var(--green-bright);font-weight:500;font-size:17.5px}
.svc p{top:262px;left:40px;width:253px;text-align:center;font-size:12.5px;line-height:1.8}
.svc .more{top:326px;width:100%;text-align:center;color:var(--green-bright);font-size:12px}

/* touch */
.touch{height:570px}
.touch .photo{inset:0;background:linear-gradient(105deg,#7d8a3a 0%,#3f6b2a 30%,#1f4f2a 48%,#1a3a6a 58%,#1e4c8e 80%,#0f2c5c 100%)}
.touch h2{left:74px;top:86px;font-size:80px;font-weight:800;line-height:1.2}
.touch p{left:74px;top:299px;width:460px;font-size:13.5px;line-height:1.7}
.touch .btn{left:80px;top:405px;width:210px;height:63px;font-size:15px;font-weight:400}

/* blog */
.blog{height:699px;background:var(--black)}
.blog .title{top:123px}
.post{top:265px;width:301px}
.post .photo{position:relative;height:236px;background:linear-gradient(170deg,#d7e2ec 0%,#8aa2c2 45%,#33507f 100%)}
.post .date{margin-top:22px;font-size:11px;display:flex;align-items:center;gap:8px}
.post .date i{width:10px;height:10px;border:1.5px solid var(--green-bright);border-radius:2px}
.post h3{font-weight:400;font-size:18px;line-height:1.2;margin-top:12px}
.post .btn{margin-top:14px;width:74px;height:27px;font-size:9.5px;text-transform:none;font-weight:400}

/* contact */
.contact{height:770px;background:var(--ink)}
.contact .band{left:913px;top:0;width:287px;height:725px;background:var(--green)}
.contact h2{left:75px;top:74px;font-size:56px;font-weight:800}
.contact .sub{left:77px;top:148px;color:var(--green-bright);font-size:20px;display:flex;align-items:center;gap:16px}
.contact .sub b{width:84px;height:2px;background:var(--green-bright)}
.contact .intro{left:80px;top:220px;width:500px;font-size:13.5px;line-height:1.65}
.field{background:var(--field);border:1px solid var(--line);font-size:13px;color:#bbb;padding:14px 20px}
.contact .submit{left:75px;top:609px;width:168px;height:49px;font-size:16px}
.contact .ring{left:636px;top:110px;width:558px;height:558px;border-radius:50%;border:3px solid var(--green-bright);background:var(--ink)}
.contact .photo{left:650px;top:124px;width:530px;height:530px;border-radius:50%;background:linear-gradient(150deg,#dbe6ef 0%,#9db0c6 40%,#3b5688 75%,#1b2f5a 100%)}

/* footer */
.footer{height:355px;background:var(--black)}
.footer .logo{left:79px;top:125px}
.social{top:273px;display:flex;gap:17px;left:105px}
.social i{width:28px;height:28px;border:1.5px solid var(--green-bright);border-radius:3px}
.fcol{top:96px}
.fcol h4{color:var(--green-bright);font-weight:400;font-size:15.5px}
.fcol h4::after{content:"";display:block;width:38px;height:2px;background:var(--white);margin-top:12px}
.fcol ul{list-style:none;margin-top:24px;font-size:13px;line-height:27px}
.fcol li{display:flex;align-items:center;gap:8px}
.fcol li::before{content:"";width:8px;height:8px;border-radius:50%;background:var(--green-bright)}
.crow{display:flex;gap:24px;font-size:12.5px;line-height:1.25;margin-bottom:16px}
.crow i{flex:none;width:26px;height:26px;border:1px solid var(--green-bright);border-radius:3px;display:flex;align-items:center;justify-content:center}
.news p{font-size:13px;line-height:1.4;margin-top:22px;width:220px}
.news .input{margin-top:20px;width:208px;height:37px;border:1.5px solid var(--green-bright);border-radius:20px;font-size:11px;color:#aaa;display:flex;align-items:center;justify-content:space-between;padding:0 4px 0 16px}
.news .input i{width:28px;height:28px;border:1.5px solid var(--white);border-radius:50%;display:flex;align-items:center;justify-content:center}
.copyright{height:63px;background:var(--green);font-size:12px;display:flex;align-items:center;justify-content:center}
</style>
</head>
<body>

<header class="topbar">
  <div class="abs call"><i><svg width="13" height="13" viewBox="0 0 24 24" fill="#fff"><path d="M6.6 10.8a15.1 15.1 0 0 0 6.6 6.6l2.2-2.2c.3-.3.7-.4 1-.2 1.1.4 2.3.6 3.6.6.6 0 1 .4 1 1V20c0 .6-.4 1-1 1A17 17 0 0 1 3 4c0-.6.4-1 1-1h3.5c.6 0 1 .4 1 1 0 1.3.2 2.5.6 3.6.1.3 0 .7-.2 1z"/></svg></i>CALL: XXXX XXX XXX</div>
  <div class="abs cta">FREE CONSULTATION</div>
</header>

<nav class="nav">
  <div class="abs logo"><i></i>BRIGHTVX</div>
  <ul class="abs">
    <li class="active">HOME</li><li>ABOUT US</li><li>SERVICES</li><li>BLOG</li><li>REVIEWS</li><li>CONTACT US</li>
  </ul>
</nav>

<section class="hero">
  <div class="photo" role="img" aria-label="Technician in a yellow helmet cleaning rooftop solar panels under a bright sky"></div>
  <div class="abs copy">
    <h2>Welcome To</h2>
    <h1>BRIGHTVX ENERGY GROUP</h1>
    <p>Lorem ipsum dolor sit amet, consectetuer adipiscing elit. Aenean commodo ligula eget dolor.</p>
    <span class="btn btn-solid">Free Consultation</span>
  </div>
</section>

<section class="features">
  <div class="abs feature" style="left:100px;width:262px">
    <svg width="56" height="52" viewBox="0 0 56 52"><circle cx="28" cy="26" r="10" fill="#5fd62a"/><g stroke="#5fd62a" stroke-width="3" stroke-linecap="round"><path d="M28 4v6M28 42v6M6 26h6M44 26h6M12 10l4 4M40 38l4 4M12 42l4-4M40 14l4-4"/></g></svg>
    Unrivaled home solar<br>and battery experience</div>
  <div class="abs vdiv" style="left:399px"></div>
  <div class="abs feature" style="left:430px;width:160px">
    <svg width="40" height="56" viewBox="0 0 40 56"><path d="M24 2 6 32h12l-4 22 20-32H22z" fill="#5fd62a"/></svg>
    Smart<br>technology</div>
  <div class="abs vdiv" style="left:619px"></div>
  <div class="abs feature" style="left:650px;width:240px">
    <svg width="58" height="52" viewBox="0 0 58 52"><rect x="2" y="8" width="54" height="38" rx="5" fill="#5fd62a"/><rect x="2" y="17" width="54" height="6" fill="#000"/><rect x="38" y="30" width="12" height="4" fill="#000"/></svg>
    Payment solutions<br>for every home</div>
  <div class="abs vdiv" style="left:921px"></div>
  <div class="abs feature" style="left:940px;width:190px;top:60px">
    <svg width="54" height="54" viewBox="0 0 54 54"><circle cx="27" cy="27" r="25" fill="#5fd62a"/><circle cx="27" cy="27" r="17" fill="none" stroke="#000" stroke-width="3"/><path d="M18 27l6 6 12-12" fill="none" stroke="#000" stroke-width="4"/></svg>
    The BrightVX<br>Guarantee</div>
</section>

<section class="about">
  <h2 class="abs">ABOUT US</h2>
  <div class="abs sub">WHO WE ARE <b></b></div>
  <p class="abs">Lorem ipsum dolor sit amet, consectetur adipiscing elit, sed do eiusmod tempor incididunt ut labore et dolore magna aliqua. Ut enim ad minim veniam, quis nostrud exercitation ullamco laboris nisi ut aliquip ex ea commodo consequat. Duis aute irure dolor in reprehenderit in voluptate velit esse cillum</p>
  <span class="abs btn btn-outline">Know More</span>
  <div class="abs ring"></div>
  <div class="photo" role="img" aria-label="Engineer in hard hat and safety vest standing on a solar roof above a city skyline"></div>
</section>

<section class="services">
  <div class="abs title"><h2>OUR SERVICES</h2><div class="sub"><b></b>WHAT WE DO<b></b></div></div>
  <div class="abs svc" style="left:73px">
    <div class="photo" role="img" aria-label="Two installers mounting solar panels"></div>
    <div class="abs power"><svg width="36" height="36" viewBox="0 0 36 36"><circle cx="18" cy="18" r="17" fill="#3fae1e"/><path d="M12 12a9 9 0 1 0 12 0" fill="none" stroke="#fff" stroke-width="3" stroke-linecap="round"/><path d="M18 8v10" stroke="#fff" stroke-width="3" stroke-linecap="round"/></svg></div>
    <h3 class="abs">SOLAR PANEL INSTALLATION</h3>
    <p class="abs">Lorem ipsum dolor sit amet, ocec tetur adipiscing elit, sed do eius mod tempor incididunt ut</p>
  </div>
  <div class="abs svc featured" style="left:434px">
    <div class="photo" role="img" aria-label="Consultant reviewing plans beside a solar array"></div>
    <div class="abs power"><svg width="36" height="36" viewBox="0 0 36 36"><circle cx="18" cy="18" r="17" fill="#3fae1e"/><path d="M12 12a9 9 0 1 0 12 0" fill="none" stroke="#fff" stroke-width="3" stroke-linecap="round"/><path d="M18 8v10" stroke="#fff" stroke-width="3" stroke-linecap="round"/></svg></div>
    <h3 class="abs">CONSULTATION SERVICES</h3>
    <p class="abs">Lorem ipsum dolor sit amet, ocec tetur adipiscing elit,</p>
    <div class="abs more">READ MORE »</div>
  </div>
  <div class="abs svc" style="left:790px">
    <div class="photo" role="img" aria-label="Two engineers inspecting a solar farm"></div>
    <div class="abs power"><svg width="36" height="36" viewBox="0 0 36 36"><circle cx="18" cy="18" r="17" fill="#3fae1e"/><path d="M12 12a9 9 0 1 0 12 0" fill="none" stroke="#fff" stroke-width="3" stroke-linecap="round"/><path d="M18 8v10" stroke="#fff" stroke-width="3" stroke-linecap="round"/></svg></div>
    <h3 class="abs">CUSTOM SOLUTIONS</h3>
    <p class="abs">Lorem ipsum dolor sit amet, ocec tetur adipiscing elit, sed do eius mod tempor incididunt ut</p>
  </div>
</section>

<section class="touch">
  <div class="photo" role="img" aria-label="Wind turbines on green fields beside a large solar panel array"></div>
  <h2 class="abs">GET IN TOUCH<br>TODAY!</h2>
  <p class="abs">Lorem ipsum dolor sit amet, consectetur adipiscing elit, sed do eiusmod tempor incididunt ut labore et dolore magna aliqua.</p>
  <span class="abs btn btn-outline">Free Consultation</span>
</section>

<section class="blog">
  <div class="abs title"><h2>LATEST BLOG</h2><div class="sub"><b></b>NEWS &amp; UPDATES<b></b></div></div>
  <article class="abs post" style="left:104px">
    <div class="photo" role="img" aria-label="Installer with a drill fitting a solar panel"></div>
    <div class="date"><i></i>JAN 25, 2023</div>
    <h3>Lorem ipsum dolor sit amet, consectetur adipiscing elit,</h3>
    <span class="btn btn-solid">Read More</span>
  </article>
  <article class="abs post" style="left:448px">
    <div class="photo" role="img" aria-label="Engineers discussing plans beside solar panels"></div>
    <div class="date"><i></i>JAN 25, 2023</div>
    <h3>Lorem ipsum dolor sit amet, consectetur adipiscing elit,</h3>
    <span class="btn btn-solid">Read More</span>
  </article>
  <article class="abs post" style="left:788px">
    <div class="photo" role="img" aria-label="Rows of solar panels along a coastline"></div>
    <div class="date"><i></i>JAN 25, 2023</div>
    <h3>Lorem ipsum dolor sit amet, consectetur adipiscing elit,</h3>
    <span class="btn btn-solid">Read More</span>
  </article>
</section>

<section class="contact">
  <div class="abs band"></div>
  <h2 class="abs">CONTACT US</h2>
  <div class="abs sub">BRIGHTVX ENERGY GROUP <b></b></div>
  <p class="abs intro">Lorem ipsum dolor sit amet, consectetur adipiscing elit, sed do eiusmod tempor incididunt ut labore et dolore magna aliqua.</p>
  <div class="abs field" style="left:73px;top:296px;width:225px;height:45px">First Name</div>
  <div class="abs field" style="left:316px;top:296px;width:226px;height:45px">Last Name</div>
  <div class="abs field" style="left:73px;top:361px;width:225px;height:45px">Phone</div>
  <div class="abs field" style="left:316px;top:361px;width:226px;height:45px">Email</div>
  <div class="abs field" style="left:73px;top:426px;width:469px;height:146px;padding-top:24px">Message</div>
  <span class="abs btn btn-solid submit">Submit</span>
  <div class="abs ring"></div>
  <div class="photo" role="img" aria-label="Installer in orange helmet working on a solar panel"></div>
</section>

<footer class="footer">
  <div class="abs logo"><i></i>BRIGHTVX</div>
  <div class="abs social"><i></i><i></i><i></i><i></i></div>
  <div class="abs fcol" style="left:383px">
    <h4>QUICK LINKS</h4>
    <ul><li>About Us</li><li>Services</li><li>Reviews</li><li>Gallery</li><li>Contact Us</li></ul>
  </div>
  <div class="abs fcol" style="left:589px">
    <h4>CONTACT US</h4>
    <div style="margin-top:24px">
      <div class="crow"><i><svg width="12" height="12" viewBox="0 0 24 24" fill="#5fd62a"><path d="M6.6 10.8a15.1 15.1 0 0 0 6.6 6.6l2.2-2.2c.3-.3.7-.4 1-.2 1.1.4 2.3.6 3.6.6.6 0 1 .4 1 1V20c0 .6-.4 1-1 1A17 17 0 0 1 3 4c0-.6.4-1 1-1h3.5c.6 0 1 .4 1 1 0 1.3.2 2.5.6 3.6.1.3 0 .7-.2 1z"/></svg></i><span>CALL US<br>8012 555 0147</span></div>
      <div class="crow"><i><svg width="12" height="10" viewBox="0 0 24 18"><rect x="1" y="1" width="22" height="16" fill="none" stroke="#5fd62a" stroke-width="2"/><path d="M1 1l11 9 11-9" fill="none" stroke="#5fd62a" stroke-width="2"/></svg></i><span>EMAIL US<br>hello@brightvxenergy.com</span></div>
      <div class="crow"><i><svg width="10" height="13" viewBox="0 0 20 26"><path d="M10 1a9 9 0 0 0-9 9c0 7 9 15 9 15s9-8 9-15a9 9 0 0 0-9-9z" fill="#5fd62a"/><circle cx="10" cy="10" r="3" fill="#000"/></svg></i><span>Address line Dummy Here<br>Address line Here</span></div>
    </div>
  </div>
  <div class="abs fcol news" style="left:882px">
    <h4>OUR NEWSLETTER</h4>
    <p>Subscribe our newsletter to get the latest news.</p>
    <div class="input">Enter Email Address<i><svg width="12" height="10" viewBox="0 0 12 10"><path d="M1 5h9M6 1l4 4-4 4" fill="none" stroke="#fff" stroke-width="1.5"/></svg></i></div>
  </div>
</footer>

<div class="copyright">Copyright © 2024 All Rights Reserved By Company name</div>

</body>
</html>
```